Used Semi Truck Website Redesign

We are redoing the website backend and would like to also do a front end redesign. I would like a Mobile and Desktop mockup for each page. The website has more mobile visitors than desktop visitors. Our competitor is http://www.haulmarketbay.example. We don't want to copy them exactly but we want a site that looks more like that. We need the functionality of that site. One big difference is that we also sell parts and trailers.

We need a redesign for front page, product detail page, search result page, content page. It is very important that the site is very easy to use on mobile devices. Our target audience is Rigline.

Feel free to use demo fonts stock images, and icons. We will purchase necessary 3rd party media when a winner is chosen.

Target Market(s)

People who want to buy used trucks.

Coding

Coded - Design and coding required

Number of Pages Required

5+ page

Requirements
Must have
• Mockup for Desktop and Mobile pages.

```html
<!DOCTYPE html>
<html lang="en">
<head>
<meta charset="utf-8">
<title>Product detail – Rigline</title>
<link href="https://fonts.googleapis.com/css2?family=Roboto:wght@400;500;700&family=Oswald:wght@400;500&display=swap" rel="stylesheet">
<style>
:root{
  --ink:#0d1a1f;
  --orange:#ff6a00;
  --text:#222;
  --muted:#8a8a8a;
  --line:#e3e3e3;
  --panel:#f4f4f4;
  --white:#fff;
  --star:#f5b400;
}
*{box-sizing:border-box;margin:0;padding:0}
html,body{width:674px;height:1200px;overflow:hidden;background:var(--white)}
body{position:relative;font-family:'Roboto',sans-serif;color:var(--text);font-size:7px}
.abs{position:absolute}
.topbar{left:0;top:0;width:674px;height:18px;background:var(--ink);color:var(--white);font-size:7px;line-height:18px}
.topbar .count{left:50px}
.topbar .links{right:50px}
.hero{left:0;top:18px;width:674px;height:142px;background:linear-gradient(90deg,#3a3d40 0%,#5a5e62 45%,#4b5563 70%,#2c3440 100%)}
.brand{left:50px;top:16px;color:var(--white);line-height:1}
.brand .name{display:flex;align-items:center;gap:5px;font-family:'Roboto',sans-serif;font-weight:500;font-size:14px;color:var(--white)}
.brand .name i{width:9px;height:9px;background:var(--orange);display:block}
.brand small{display:block;font-size:6.5px;margin-top:3px;color:var(--white)}
.nav{left:311px;top:22px;color:var(--white);font-size:7px;display:flex;align-items:center;gap:10px}
.nav .sep{width:1px;height:9px;background:#888}
.social{display:flex;gap:5px;margin-left:4px}
.social i{width:14px;height:14px;border-radius:50%;background:#1b1b1b;display:block}
.promo{left:498px;top:4px;width:126px;height:33px;background:rgba(20,28,34,.85);text-align:center;padding-top:6px}
.promo b{display:block;font-family:'Oswald',sans-serif;font-weight:500;color:var(--orange);font-size:13px;line-height:1}
.promo span{font-family:'Oswald',sans-serif;color:var(--white);font-size:7px}
.hero h1{left:0;width:674px;top:78px;line-height:1;text-align:center;color:var(--white);font-family:'Oswald',sans-serif;font-weight:400;font-size:19px}
.crumb{left:0;width:674px;top:99px;line-height:1;text-align:center;color:var(--white);font-size:8px}
.photo-main{left:57px;top:174px;width:267px;height:176px;border:1px solid var(--line);background:var(--white)}
.photo-main div{position:absolute;left:40px;top:22px;width:190px;height:130px;background:radial-gradient(ellipse,#9a9ea3 0%,#c9ccd0 55%,#fff 75%)}
.thumbs{left:57px;top:355px;display:flex;gap:5px}
.thumbs div{width:50px;height:44px;border:1px solid var(--line);background:radial-gradient(circle,#8d9196 0%,#d5d7da 45%,#fff 70%)}
.info{left:342px;top:186px;width:280px}
.info h2{font-weight:400;font-size:14px}
.stars{color:var(--star);font-size:7px;letter-spacing:1px;margin-top:2px}
.price{font-size:13px;margin-top:2px}
.price span{color:var(--orange)}
.info p{font-size:6.5px;line-height:11px;margin-top:4px}
.specs{list-style:none;margin-top:10px;font-size:6.5px}
.specs li{height:12px}
.specs span{color:var(--muted)}
.tabs{left:57px;top:429px;width:561px;height:90px;border:1px solid var(--line)}
.tabs .bar{position:absolute;left:-1px;top:-1px;width:58px;height:2px;background:var(--orange)}
.tabs nav{position:absolute;left:11px;top:12px;display:flex;gap:17px;font-size:7.5px}
.tabs nav .on{color:var(--orange)}
.tabs p{position:absolute;left:9px;top:30px;width:540px;font-size:6.5px;line-height:11.5px}
.contact{left:0;top:519px;width:674px;height:263px;background:var(--panel)}
.contact h3{position:absolute;top:19px;width:674px;text-align:center;font-weight:400;font-size:12px}
.field{position:absolute;background:var(--white);border:1px solid var(--line);font-size:6.5px;padding:0 11px;line-height:20px}
.send{position:absolute;left:170px;top:214px;width:337px;height:23px;background:var(--orange);color:var(--white);text-align:center;line-height:23px;font-size:7.5px}
.newsletter{position:absolute;left:170px;top:195px;font-size:6.5px;display:flex;align-items:center;gap:7px}
.newsletter i{width:7px;height:7px;border:1px solid #aaa;background:var(--white);display:block}
.captcha{position:absolute;right:0;top:0;width:62px;height:20px;background:#e8e8e8;font-family:'Oswald',sans-serif;font-size:11px;line-height:20px;text-align:center;color:#111}
.similar-title{left:0;width:674px;top:809px;text-align:center;font-weight:400;font-size:14px}
.card{top:838px;width:138px}
.card .img{height:104px}
.card h4{font-weight:400;font-size:8px;margin-top:9px}
.card span{color:var(--muted);font-size:7px}
.dealer{left:0;top:997px;width:674px;height:49px;background:var(--orange);color:var(--white)}
.dealer svg{position:absolute;left:44px;top:13px}
.dealer h4{position:absolute;left:68px;top:10px;font-weight:400;font-size:12px}
.dealer p{position:absolute;left:69px;top:27px;font-size:6.5px}
.dealer .btn{position:absolute;left:534px;top:14px;width:86px;height:22px;background:var(--ink);font-size:6.5px;text-align:center;line-height:22px}
.footer{left:0;top:1046px;width:674px;height:154px;background:var(--ink);color:var(--white)}
.col{position:absolute;top:24px}
.col h5{font-weight:400;font-size:9px;margin-bottom:8px}
.col li{list-style:none;font-size:6.5px;height:16px;display:flex;align-items:center;gap:6px}
.col li .dot{width:13px;height:13px;border-radius:50%;display:block}
.tweet{font-size:6.5px;line-height:10px;display:flex;gap:6px;padding-bottom:8px;margin-bottom:8px;border-bottom:1px solid #243238;width:144px}
.tweet i{width:8px;height:8px;border-radius:50%;background:#1da1f2;flex:none;margin-top:1px}
.footer .rule{position:absolute;left:45px;top:129px;width:575px;height:1px;background:#243238}
.footer .copy{position:absolute;left:48px;top:137px;font-size:6.5px}
.footer .legal{position:absolute;right:55px;top:137px;font-size:6.5px;font-weight:500}
.totop{left:632px;top:1167px;width:18px;height:18px;border-radius:50%;background:var(--orange)}
</style>
</head>
<body>

<header class="abs topbar">
  <span class="abs count">256,140 trucks and trailers for sale</span>
  <span class="abs links">MyTrader: Login | Register | Find a Dealer | Dealer Login</span>
</header>

<section class="abs hero" role="img" aria-label="Blue semi truck on a highway, dark photo banner">
  <div class="abs brand"><span class="name"><i></i>Rigline</span><small>sell parts and trailers</small></div>
  <nav class="abs nav">
    <span>Find</span><i class="sep"></i><span>Sell</span><i class="sep"></i><span>Research</span>
    <span class="social"><i></i><i></i><i></i><i></i></span>
  </nav>
  <div class="abs promo"><b>CLICK HERE</b><span>WWW.EXAMPLE.COM</span></div>
  <h1 class="abs">Product detail</h1>
  <div class="abs crumb">Home / Product Detail</div>
</section>

<div class="abs photo-main"><div role="img" aria-label="Assorted truck engine parts"></div></div>
<div class="abs thumbs">
  <div role="img" aria-label="Parts thumbnail"></div>
  <div role="img" aria-label="Parts thumbnail"></div>
  <div role="img" aria-label="Springs thumbnail"></div>
  <div role="img" aria-label="Camshaft thumbnail"></div>
  <div role="img" aria-label="Bearing thumbnail"></div>
</div>

<section class="abs info">
  <h2>Sell parts</h2>
  <div class="stars">★★★★★</div>
  <div class="price">Price: <span>$59,500</span></div>
  <p>Lorem ipsum dolor sit amet, consectetuer adipiscing elit, sed diam nonummy nibh euis-mod tinc amet risus consectetur, non consectetur nisl finibus. Ut ac eros quis mi volutpat cursus vel non risus. Lorem ipsum dolor sit amet, consectetuer .</p>
  <ul class="specs">
    <li>Year: <span>2016</span></li>
    <li>Make: <span>Veltrano-Kessler</span></li>
    <li>Model: <span>ROADLINE 2500</span></li>
    <li>Class: <span>CLASS 3 (GVW 10001 - 14000)</span></li>
    <li>Category : <span>Passenger Van</span></li>
    <li>Engine Make: <span>VELTRANO KESSLER</span></li>
    <li>Mileage: <span>14000</span></li>
    <li>New/Used: <span>U</span></li>
    <li>Fuel Type: <span>Diesel</span></li>
    <li>Price: <span>59500</span></li>
  </ul>
</section>

<section class="abs tabs">
  <i class="bar"></i>
  <nav><span class="on">Description</span><span>Review(0)</span><span>Add Tags</span></nav>
  <p>Porem ipsum dolor sit amet, consectetuer adipiscing elit, sed diam nonummy nibh euismod tincidunt ut laoreet dolore magna aliquam erat volutpat. Ut wisi enim ad minim veniam, quis nostrud exerci tation ullamcorper suscipit lobortis nisl ut aliquip ex ea commodo consequat. Lorem ipsum dolor sit amet, consectetuer adipis-cing elit, sed diam nonummy nibh euismod tincidunt ut laoreet dolore magna aliquam.</p>
</section>

<section class="abs contact">
  <h3>Contact Seller</h3>
  <div class="field" style="left:170px;top:43px;width:165px">Contact me<span style="float:right">▾</span></div>
  <div class="field" style="left:339px;top:43px;width:165px">Email</div>
  <div class="field" style="left:170px;top:67px;width:165px">Name</div>
  <div class="field" style="left:339px;top:67px;width:165px">Phone</div>
  <div class="field" style="left:170px;top:92px;width:334px;height:69px">Comments</div>
  <div class="field" style="left:170px;top:166px;width:334px">Type image number<span class="captcha">6on56y</span></div>
  <div class="newsletter"><i></i>Would you like to get our newsletter and special offers via email?</div>
  <div class="send">SEND</div>
</section>

<h3 class="abs similar-title">Find Similar Trucks</h3>
<article class="abs card" style="left:50px"><div class="img" role="img" aria-label="Engine components" style="background:linear-gradient(135deg,#6f757b,#c4c8cc)"></div><h4>2016 Harlow H-SERIES</h4><span>$37,500.00</span></article>
<article class="abs card" style="left:196px"><div class="img" role="img" aria-label="Black semi truck on road" style="background:linear-gradient(160deg,#9aa4ad,#2b2f33)"></div><h4>2016 Harlow H-SERIES</h4><span>$37,500.00</span></article>
<article class="abs card" style="left:341px"><div class="img" role="img" aria-label="Truck engine close-up" style="background:linear-gradient(135deg,#55595d,#b9bcbf)"></div><h4>2016 Harlow H-SERIES</h4><span>$37,500.00</span></article>
<article class="abs card" style="left:486px"><div class="img" role="img" aria-label="Orange truck on dirt road" style="background:linear-gradient(180deg,#7d9bb5,#e07a2e 60%,#9b8a6e)"></div><h4>2016 Harlow H-SERIES</h4><span>$37,500.00</span></article>

<section class="abs dealer">
  <svg width="18" height="24" viewBox="0 0 18 24"><path d="M9 0a9 9 0 0 1 9 9c0 6-9 15-9 15S0 15 0 9a9 9 0 0 1 9-9z" fill="#fff"/><circle cx="9" cy="9" r="3.5" fill="#ff6a00"/></svg>
  <h4>Find a Dealer</h4>
  <p>Find Commercial Truck dealers by name, make and location.</p>
  <div class="btn">FIND A DEALER</div>
</section>

<footer class="abs footer">
  <div class="col" style="left:45px"><h5>Explore Our Site</h5><ul><li>→ Trucks for Sale</li><li>→ Truck Resources</li><li>→ New Truck Models</li><li>→ Check Truck Prices</li></ul></div>
  <div class="col" style="left:188px"><h5>Sell Truck &amp; Parts</h5><ul><li>→ Private Truck Sellers</li><li>→ Truck Dealers</li><li>→ Advertise on Commercial</li><li>→ sell parts</li></ul></div>
  <div class="col" style="left:352px"><h5>Follow Us</h5><ul>
    <li style="height:19px"><i class="dot" style="background:#f57c00"></i>Blog</li>
    <li style="height:19px"><i class="dot" style="background:#3b5998"></i>Friendbook</li>
    <li style="height:19px"><i class="dot" style="background:#1da1f2"></i>Chirper</li>
    <li style="height:19px"><i class="dot" style="background:#e53935"></i>ClipTube</li></ul></div>
  <div class="col" style="left:476px"><h5>Chirper Feed</h5>
    <div class="tweet"><i></i><span>@ Nulla consequat massa s enim donec pede justo,</span></div>
    <div class="tweet" style="border:0"><i></i><span>@ Nulla consequat massa s enim donec pede justo,</span></div>
  </div>
  <i class="rule"></i>
  <div class="copy">Copyright 2016 | All Right Reserved</div>
  <div class="legal">Terms &amp; Conditions | Privacy Policy</div>
</footer>
<div class="abs totop"><svg width="18" height="18" viewBox="0 0 18 18"><path d="M6 10.5l3-3 3 3" stroke="#fff" stroke-width="1.4" fill="none"/></svg></div>

</body>
</html>
```